Parkinson's Disease Progression

Visually describe the rate of Parkinson progression in the first 15 years following diagnosis. Title: "Patient-Perceived Progression of Parkinsonism"

The attached figure names "meanqol" is the curve that should serve as the basis of this graphic. Everything else-- color, labels, font, etc. describe this curve.
Thank you!

Target Market(s)

People with Parkisnon's Disease, neurologists, family members.

Font styles to use
Sans Serif

Requirements
Must have
• Must have the lines going through these exact numbers
Excellent -- 502
Very good- 661
Good- 895
Fair- 1268
Poor- 1655

LABELS:
Title: "Patient-Perceived Progression of Parkinsonism"
"SWI-TC (Self-Logged Wellbeing Index for Tremor Conditions)" should be the label on the left.
"Quality of Life" should be the label on the right
"Years Since Diagnosis" should be the label on the bottom
Nice to have
• A color scheme that goes from GOOD (low numbers) to BAD (high numbers).

Easy to read (elderly)

```html
<!DOCTYPE html>
<html lang="en">
<head>
<meta charset="utf-8">
<title>Patient-Perceived Progression of Parkinsonism</title>
<link rel="stylesheet" href="https://fonts.googleapis.com/css2?family=Arimo:wght@400&family=Barlow+Condensed:wght@500;700&display=swap">
<style>
  :root {
    --ink: #000000;
    --canvas-edge: #ececec;
    --canvas-center: #ffffff;
    --band-poor: #ff8a8a;
    --band-fair: #fcc18c;
    --band-good: #f8e3b5;
    --band-very-good: #b8ffb8;
    --band-excellent: #7aeb7a;
    --value-poor: #f88a8a;
    --value-fair: #f9c08a;
    --value-good: #f8e2b4;
    --value-very-good: #7ddc7a;
    --value-excellent: #12a85a;
  }
  html, body { margin: 0; padding: 0; overflow: hidden; }
  body { width: 1200px; height: 880px; }
  .chart-canvas {
    position: relative;
    width: 1200px;
    height: 880px;
    box-sizing: border-box;
    border: 1px solid #555;
    background: radial-gradient(ellipse at center, var(--canvas-center) 60%, var(--canvas-edge) 100%);
  }
  .chart-canvas svg { display: block; }
  .chart-title { font-family: "Barlow Condensed", sans-serif; font-weight: 500; font-size: 25px; fill: var(--ink); }
  .tick-label { font-family: "Arimo", sans-serif; font-size: 22px; fill: var(--ink); }
  .axis-title { font-family: "Arimo", sans-serif; font-size: 26px; fill: var(--ink); }
  .band-label { font-family: "Arimo", sans-serif; font-size: 16px; fill: var(--ink); }
  .threshold-value { font-family: "Barlow Condensed", sans-serif; font-weight: 700; font-size: 31px; }
  .axis-line { stroke: var(--ink); stroke-width: 1; fill: none; }
  .band-divider { stroke: var(--ink); stroke-width: 0.8; stroke-dasharray: 3 2; }
  .mean-curve { stroke: var(--ink); stroke-width: 1.6; fill: none; stroke-linejoin: round; stroke-linecap: round; }
  .confidence-bound { stroke: var(--ink); stroke-width: 0.8; fill: none; stroke-dasharray: 3 2.5; }
</style>
</head>
<body>
<div class="chart-canvas">
  <svg width="1198" height="878" viewBox="0 0 1200 880" role="img" aria-label="Line chart of SWI-TC score over 15 years since diagnosis with quality of life bands">
    <text class="chart-title" x="625" y="68" text-anchor="middle">Patient-Perceived Progression of Parkinsonism</text>

    <!-- quality of life bands -->
    <g class="quality-bands">
      <rect x="256" y="90.6" width="738.4" height="181.2" fill="var(--band-poor)"/>
      <rect x="256" y="271.8" width="738.4" height="121.5" fill="var(--band-fair)"/>
      <rect x="256" y="393.3" width="738.4" height="108.7" fill="var(--band-good)"/>
      <rect x="256" y="502" width="738.4" height="59.7" fill="var(--band-very-good)"/>
      <rect x="256" y="561.7" width="738.4" height="170.5" fill="var(--band-excellent)"/>
      <line class="band-divider" x1="256" y1="271.8" x2="994.4" y2="271.8"/>
      <line class="band-divider" x1="256" y1="393.3" x2="994.4" y2="393.3"/>
      <line class="band-divider" x1="256" y1="502" x2="994.4" y2="502"/>
      <line class="band-divider" x1="256" y1="561.7" x2="994.4" y2="561.7"/>
      <path class="axis-line" d="M256 90.6 V732.2 H994.4"/>
    </g>

    <g class="band-labels">
      <text class="band-label" x="284.6" y="149">Poor</text>
      <text class="band-label" x="287.8" y="297">Fair</text>
      <text class="band-label" x="280.3" y="420">Good</text>
      <text class="band-label" x="263.3" y="525.5">Very good</text>
      <text class="band-label" x="267.5" y="587.5">Excellent</text>
    </g>

    <!-- y axis -->
    <g class="y-axis">
      <line class="axis-line" x1="240" y1="92.2" x2="256" y2="92.2"/>
      <line class="axis-line" x1="240" y1="160.4" x2="256" y2="160.4"/>
      <line class="axis-line" x1="240" y1="229.1" x2="256" y2="229.1"/>
      <line class="axis-line" x1="240" y1="297.4" x2="256" y2="297.4"/>
      <line class="axis-line" x1="240" y1="373" x2="256" y2="373"/>
      <line class="axis-line" x1="240" y1="448.7" x2="256" y2="448.7"/>
      <line class="axis-line" x1="240" y1="524.9" x2="256" y2="524.9"/>
      <line class="axis-line" x1="240" y1="600.6" x2="256" y2="600.6"/>
      <line class="axis-line" x1="240" y1="676.2" x2="256" y2="676.2"/>
      <text class="tick-label" x="234" y="113" text-anchor="end">1800</text>
      <text class="tick-label" x="234" y="186" text-anchor="end">1600</text>
      <text class="tick-label" x="234" y="245.5" text-anchor="end">1400</text>
      <text class="tick-label" x="226" y="311.5" text-anchor="end">1200</text>
      <text class="tick-label" x="228" y="380.5" text-anchor="end">1000</text>
      <text class="tick-label" x="231" y="457" text-anchor="end">800</text>
      <text class="tick-label" x="232" y="533" text-anchor="end">600</text>
      <text class="tick-label" x="233" y="609" text-anchor="end">400</text>
      <text class="tick-label" x="227" y="684" text-anchor="end">200</text>
    </g>

    <g class="threshold-values">
      <text class="threshold-value" x="241" y="146" text-anchor="end" fill="var(--value-poor)">1655</text>
      <text class="threshold-value" x="238" y="282" text-anchor="end" fill="var(--value-fair)">1268</text>
      <text class="threshold-value" x="240" y="418" text-anchor="end" fill="var(--value-good)">895</text>
      <text class="threshold-value" x="234" y="505" text-anchor="end" fill="var(--value-very-good)">661</text>
      <text class="threshold-value" x="238" y="584.5" text-anchor="end" fill="var(--value-excellent)">502</text>
    </g>

    <!-- x axis -->
    <g class="x-axis">
      <line class="axis-line" x1="278.7" y1="732.2" x2="278.7" y2="748"/>
      <line class="axis-line" x1="508.4" y1="732.2" x2="508.4" y2="748"/>
      <line class="axis-line" x1="738.1" y1="732.2" x2="738.1" y2="748"/>
      <line class="axis-line" x1="967.7" y1="732.2" x2="967.7" y2="748"/>
      <text class="tick-label" x="278.7" y="789" text-anchor="middle" font-size="24">0</text>
      <text class="tick-label" x="508.4" y="789" text-anchor="middle" font-size="24">5</text>
      <text class="tick-label" x="738.1" y="789" text-anchor="middle" font-size="24">10</text>
      <text class="tick-label" x="967.7" y="789" text-anchor="middle" font-size="24">15</text>
    </g>

    <!-- progression curve -->
    <polyline class="confidence-bound" points="283,506.3 319.7,495.6 373,463.6 426.3,426.3 479.6,391.7 522.2,379.4 586.2,373 639.5,357 692.8,319.7 756.7,266.5 826,218.5 895.3,170.5 967.7,105"/>
    <polyline class="confidence-bound" points="283,622.4 319.7,564.9 373,506.3 426.3,458.3 479.6,426.3 522.2,415.7 586.2,410.3 639.5,394.4 692.8,362.4 746.1,325.1 799.3,290.4 852.6,266.5 905.9,255.8 967.7,266.5"/>
    <polyline class="mean-curve" points="283,563.8 351.7,502 405,461 458.3,426.3 506.3,400.7 554.2,394.4 586.2,392.8 639.5,378.4 692.8,346.4 746.1,303.8 786,271.8 831.3,245.1 879.3,223.8 967.7,186"/>

    <!-- axis titles -->
    <text class="axis-title" x="625" y="843" text-anchor="middle" font-size="27">Years since diagnosis</text>
    <text class="axis-title" transform="translate(156 486) rotate(-90)" text-anchor="middle">SWI-TC</text>
    <text class="axis-title" transform="translate(1033 413.5) rotate(-90)" text-anchor="middle">QUALITY OF LIFE</text>
  </svg>
</div>
</body>
</html>
```